Hello again

I have a few Logos I am looking to add

Target Market(s)

MediSpa

Industry/Entity Type

Medispa

Contact Information for Business Card

Dana Whitcombe, Owner/Medical Aesthetician, 403-812-3957, Unit 148 - 1920 5 st NW, T3K 1M7 Calgary, AB., www.LarkMediSpa.ca ....QR codes are attached I do really like the former business card but everything was in teal, gold and white.

```html
<!DOCTYPE html>
<html lang="en">
<head>
<meta charset="utf-8">
<title>Lark MediSpa – Business Cards</title>
<link href="https://fonts.googleapis.com/css2?family=Montserrat:wght@400;500;700&display=swap" rel="stylesheet">
<style>
  :root {
    --stage: #2b2b2b;
    --card: #050505;
    --card-edge: #1a1a1a;
    --gold: #d4b45a;
    --white: #ffffff;
    --soft-white: #e8e8e8;
  }
  * { margin: 0; padding: 0; box-sizing: border-box; }
  html, body {
    width: 1200px; height: 875px; overflow: hidden;
    background: var(--stage);
    font-family: "Montserrat", sans-serif;
  }
  .canvas { position: relative; width: 1200px; height: 875px; }

  .card {
    position: absolute;
    width: 540px; height: 309px;
    background: var(--card);
    border: 1px solid var(--card-edge);
    border-radius: 18px;
    overflow: hidden;
    box-shadow: 0 18px 40px rgba(0,0,0,.45);
  }
  .card--front { left: 50px; top: 110px; }
  .card--back  { left: 610px; top: 450px; }

  .brand {
    position: absolute;
    display: flex; align-items: center; gap: 12px;
  }
  .brand__dot {
    width: 14px; height: 14px; border-radius: 50%;
    background: var(--gold);
  }
  .brand__name {
    font-weight: 500;
    color: var(--white);
    letter-spacing: .02em;
    white-space: nowrap;
  }
  .brand__tagline {
    position: absolute;
    color: var(--gold);
    font-weight: 400;
    letter-spacing: .28em;
    text-transform: uppercase;
    white-space: nowrap;
  }

  .card--front .brand { left: 112px; top: 128px; }
  .card--front .brand__name { font-size: 38px; }
  .card--front .brand__tagline { left: 138px; top: 186px; font-size: 9.5px; }

  .card--back .brand { left: 40px; top: 108px; }
  .card--back .brand__name { font-size: 30px; }
  .card--back .brand__tagline { left: 66px; top: 154px; font-size: 7.5px; }

  .holder {
    position: absolute; right: 36px; top: 34px; text-align: right;
  }
  .holder__name {
    color: var(--gold); font-weight: 700; font-size: 21px; letter-spacing: .01em;
  }
  .holder__role {
    color: var(--soft-white); font-size: 10.5px; margin-top: 3px;
  }

  .contact {
    position: absolute; left: 40px; bottom: 30px;
    color: var(--soft-white); font-size: 11px; line-height: 1.55;
  }
  .contact__address { margin-bottom: 4px; }
  .contact__row { display: flex; align-items: center; gap: 9px; }
  .contact__icon { width: 11px; height: 11px; flex: none; }
</style>
</head>
<body>
<main class="canvas">

  <section class="card card--front" aria-label="Business card front">
    <div class="brand">
      <span class="brand__dot"></span>
      <span class="brand__name">Lark MediSpa</span>
    </div>
    <span class="brand__tagline">Skin &amp; Laser Specialists</span>
  </section>

  <section class="card card--back" aria-label="Business card back">
    <div class="holder">
      <p class="holder__name">Dana Whitcombe</p>
      <p class="holder__role">Owner/Medical Aesthetician</p>
    </div>

    <div class="brand">
      <span class="brand__dot"></span>
      <span class="brand__name">Lark MediSpa</span>
    </div>
    <span class="brand__tagline">Skin &amp; Laser Specialists</span>

    <div class="contact">
      <p class="contact__address">Unit 148 - 1920 5 st NW<br>Calgary, AB T3K 1M7 Canada</p>
      <p class="contact__row">
        <svg class="contact__icon" viewBox="0 0 12 12" aria-hidden="true"><path fill="#d4b45a" d="M2.4 1h2l1 2.6-1.3.9a6 6 0 0 0 3.4 3.4l.9-1.3 2.6 1v2A1.4 1.4 0 0 1 9.6 11 8.6 8.6 0 0 1 1 2.4 1.4 1.4 0 0 1 2.4 1z"/></svg>
        403-812-3957
      </p>
      <p class="contact__row">
        <svg class="contact__icon" viewBox="0 0 12 12" aria-hidden="true"><rect x="1" y="2.5" width="10" height="7" rx="1" fill="#d4b45a"/><path d="M1.5 3l4.5 3.5L10.5 3" fill="none" stroke="#050505" stroke-width="1"/></svg>
        dana@larkmedispa.ca
      </p>
      <p class="contact__row">
        <svg class="contact__icon" viewBox="0 0 12 12" aria-hidden="true"><circle cx="6" cy="6" r="5" fill="none" stroke="#d4b45a" stroke-width="1.2"/><path d="M1 6h10M6 1c-2.2 2.8-2.2 7.2 0 10M6 1c2.2 2.8 2.2 7.2 0 10" fill="none" stroke="#d4b45a" stroke-width="1"/></svg>
        www.LarkMediSpa.ca
      </p>
    </div>
  </section>

</main>
</body>
</html>
```